Maple Sprout Menu (Vegetarian Restaurant Concept)

Maple Sprout is a new concept fast casual restaurant
renders are attached so you can see the style of restaurant
Maple Sprowt is a vibrant and modern Vegetarian fast casual restaurant concept that mixes fresh food, energy, great décor, and a comfortable, welcoming atmosphere to provide a memorable and all Vegetarian dining experience.
Our Mission is to be top of mind when consumers think Vegetarian food!
Target Market(s)
the menu is vegetarian and appeals to a broad demographic in USA
Colors
Designer to choose colors to be used in the design.
Requirements
Must have
- well colored and well laid out menu - should not be cartoonish
Nice to have
- For Phots please use the shots in this file:
- https://www.filecrate-example.net/sh/kq7trm2wzl4pnad/BBBxT_qPwLdRNVoE_KMS_Tb?dl=0
- note these are untouched and you are free to change as needed
Should not have
- Should not be cartoonish - nor kives, forks etc in the design

```html
<!DOCTYPE html>
<html lang="en">
<head>
<meta charset="utf-8">
<title>Maple Sprowt Menu</title>
<link rel="stylesheet" href="https://fonts.googleapis.com/css2?family=Catamaran:wght@400;600;700&display=swap">
<style>
  :root {
    --leaf: #7cbf45;
    --leaf-deep: #5c9f38;
    --ink: #1d1d1b;
    --frame: #2b2b2b;
    --paper: #ffffff;
  }
  * { box-sizing: border-box; margin: 0; padding: 0; }
  html, body { width: 927px; height: 1200px; overflow: hidden; background: var(--paper); }
  body { font-family: "Catamaran", sans-serif; color: var(--ink); }

  .menu { position: relative; width: 927px; height: 1200px; }
  .outer-frame { position: absolute; left: 16px; top: 16px; right: 16px; bottom: 16px; border: 1.5px solid var(--leaf); }
  .inner-frame { position: absolute; left: 27px; top: 27px; width: 873px; height: 1146px; border: 1.5px solid var(--frame); }

  .brand { position: absolute; left: 76px; top: 48px; width: 328px; text-align: center; }
  .brand-dot { width: 120px; height: 120px; border-radius: 50%; background: var(--leaf); margin: 20px auto 34px; }
  .brand-name { font-weight: 700; font-size: 44px; line-height: 1; color: var(--ink); }

  .section { position: absolute; border: 1.5px solid var(--leaf); padding: 26px 8px 0 8px; }
  .section-title {
    position: absolute; top: -20px; left: 20px; padding: 0 4px;
    background: var(--paper); color: var(--leaf-deep);
    font-weight: 600; font-size: 27px; line-height: 34px;
  }

  .salads { left: 75px; top: 342px; width: 326px; height: 456px; }
  .toasts { left: 75px; top: 825px; width: 326px; height: 228px; padding-top: 24px; }
  .soups { left: 75px; top: 1077px; width: 326px; height: 64px; padding-top: 22px; }
  .burgers { left: 464px; top: 92px; width: 383px; height: 433px; padding: 24px 10px 0 12px; }
  .bowls { left: 464px; top: 561px; width: 383px; height: 282px; padding: 32px 10px 0 12px; }
  .dessert { left: 464px; top: 881px; width: 383px; height: 218px; padding: 28px 10px 0 12px; }

  .item { margin-bottom: 12px; }
  .item-lead { font-weight: 600; font-size: 20.5px; line-height: 25px; white-space: nowrap; }
  .item-line { display: flex; align-items: flex-end; font-weight: 600; font-size: 20.5px; line-height: 25px; }
  .item-name { white-space: nowrap; }
  .leader { flex: 1; border-bottom: 2px dashed var(--ink); margin: 0 7px 9px; min-width: 10px; }
  .price { font-weight: 700; font-size: 19.5px; white-space: nowrap; }
  .item-desc { font-size: 16.5px; line-height: 21.8px; margin-top: 7px; }

  .salads .item { margin-bottom: 9px; }
  .toasts .item { margin-bottom: 22px; }
  .burgers .item { margin-bottom: 16px; }
  .bowls .item { margin-bottom: 19px; }
  .dessert .item { margin-bottom: 20px; }
</style>
</head>
<body>
<main class="menu">
  <div class="outer-frame"></div>
  <div class="inner-frame"></div>

  <header class="brand">
    <div class="brand-dot"></div>
    <div class="brand-name">Maple Sprowt</div>
  </header>

  <section class="section salads">
    <h2 class="section-title">Salads</h2>
    <div class="item">
      <div class="item-line"><span class="item-name">Brussel Sprouts Caesar</span><span class="leader"></span><span class="price">$10.90</span></div>
      <p class="item-desc">little gem romaine, toasted torn bread,<br>parmigiano reggiano</p>
    </div>
    <div class="item">
      <div class="item-line"><span class="item-name">Heirloom Beet Salad</span><span class="leader"></span><span class="price">$10.90</span></div>
      <p class="item-desc">shaved chioggia beet, roasted golden<br>beet, red quinoa, little gem, arugula,<br>lemon vinaigrette</p>
    </div>
    <div class="item">
      <div class="item-lead">Zesty Black Bean and Corn</div>
      <div class="item-line"><span class="item-name">Salad in Lettuce Cups</span><span class="leader"></span><span class="price">$10.90</span></div>
      <p class="item-desc">black beans, avocado and roasted corn<br>topped with feta crumbles<br>in butter lettuce</p>
    </div>
    <div class="item">
      <div class="item-line"><span class="item-name">Green, Red and White</span><span class="leader"></span><span class="price">$10.90</span></div>
      <p class="item-desc">spring leaves, cherry tomatoes, avocado,<br>roasted almond and goat cheese</p>
    </div>
  </section>

  <section class="section toasts">
    <h2 class="section-title">Toasts</h2>
    <div class="item" style="margin-bottom:16px">
      <div class="item-line"><span class="item-name">Everything Avocado Toast</span><span class="leader"></span><span class="price">$5.90</span></div>
      <p class="item-desc">avocado on whole grain toast with our<br>signature spice blend</p>
    </div>
    <div class="item" style="margin-bottom:25px">
      <div class="item-line"><span class="item-name">Tomato &amp; Beet Bruschetta</span><span class="leader"></span><span class="price">$5.90</span></div>
    </div>
    <div class="item">
      <div class="item-lead">Vegetable Melt on</div>
      <div class="item-line"><span class="item-name">Garlic Toast</span><span class="leader"></span><span class="price">$5.90</span></div>
    </div>
  </section>

  <section class="section soups">
    <h2 class="section-title">Soups</h2>
    <div class="item">
      <div class="item-line"><span class="item-name">Black Bean Chowder</span><span class="leader"></span><span class="price">$5.90</span></div>
    </div>
  </section>

  <section class="section burgers">
    <h2 class="section-title">Burgers, Wraps &amp; Sandwiches</h2>
    <div class="item">
      <div class="item-lead">Sweet Potato, Black Bean</div>
      <div class="item-lead">Veggie Burgers with</div>
      <div class="item-line"><span class="item-name">Cabbage - Pepita Slaw</span><span class="leader"></span><span class="price">$10.90</span></div>
    </div>
    <div class="item">
      <div class="item-lead">Roasted Veggie, Arugula</div>
      <div class="item-line"><span class="item-name">and Hummus Wraps</span><span class="leader"></span><span class="price">$10.90</span></div>
    </div>
    <div class="item">
      <div class="item-line"><span class="item-name">Garden Burger</span><span class="leader"></span><span class="price">$10.90</span></div>
    </div>
    <div class="item">
      <div class="item-line"><span class="item-name">Beans and Greens Quesadillas</span><span class="leader"></span><span class="price">$10.90</span></div>
      <p class="item-desc">greens, Mexican cheese, beans and<br>avocado, with salsa</p>
    </div>
    <div class="item">
      <div class="item-line"><span class="item-name">Veggie Burrito</span><span class="leader"></span><span class="price">$10.90</span></div>
      <p class="item-desc">greens, Mexican cheese, beans, brown<br>rice, roasted chili corn and avocado, with<br>ancho chili salsa, wheat tortilla</p>
    </div>
  </section>

  <section class="section bowls">
    <h2 class="section-title">Bowls</h2>
    <div class="item">
      <div class="item-lead">Roasted Vegetable and</div>
      <div class="item-line"><span class="item-name">Spinach Bowl</span><span class="leader"></span><span class="price">$10.90</span></div>
    </div>
    <div class="item">
      <div class="item-lead">Sugar Snap Pea and</div>
      <div class="item-line"><span class="item-name">Carrot Soba Noodles</span><span class="leader"></span><span class="price">$10.90</span></div>
    </div>
    <div class="item">
      <div class="item-lead">Whole Grain and Vegetable</div>
      <div class="item-line"><span class="item-name">Buddha Bowl</span><span class="leader"></span><span class="price">$10.90</span></div>
    </div>
    <div class="item">
      <div class="item-line"><span class="item-name">Orange and Pistacio Quinoa</span><span class="leader"></span><span class="price">$10.90</span></div>
    </div>
  </section>

  <section class="section dessert">
    <h2 class="section-title">Dessert</h2>
    <div class="item">
      <div class="item-lead">Strawberry Balsamic</div>
      <div class="item-line"><span class="item-name">Ice Cream Sundae</span><span class="leader"></span><span class="price">$5.90</span></div>
    </div>
    <div class="item">
      <div class="item-line"><span class="item-name">Exotic Fruit Bowl</span><span class="leader"></span><span class="price">$5.90</span></div>
    </div>
    <div class="item">
      <div class="item-lead">White and Dark Oatmeal</div>
      <div class="item-line"><span class="item-name">Cookie</span><span class="leader"></span><span class="price">$5.90</span></div>
    </div>
  </section>
</main>
</body>
</html>
```